Marlowe Creative Works Business Card Design

We need a double-sided business card for our company Marlowe Creative Works. Our slogan is "Simple Online Solutions." We are looking for a techy, cutting-edge but simple card that looks modern and sleek. We have a black logo attached and would prefer a lighter background to make our logo stand out. We like nice accents to make it pop out and make our clients remember our card.

On the back side, we just want our logo, slogan and website. Again, something very simple. Make the logo big on the back.

```html
<!DOCTYPE html>
<html lang="en">
<head>
<meta charset="utf-8">
<title>Marlowe Creative Works – Business Card</title>
<link href="https://fonts.googleapis.com/css2?family=Jura:wght@400;500;600&family=Michroma&display=swap" rel="stylesheet">
<style>
  :root {
    --backdrop: #a7b6b0;
    --card: #f4f6f4;
    --ink: #111111;
    --teal: #4b7068;
  }
  html, body {
    margin: 0;
    width: 1200px;
    height: 848px;
    overflow: hidden;
    background: var(--backdrop);
  }
  .canvas {
    position: relative;
    width: 1200px;
    height: 848px;
  }
  .card {
    position: absolute;
    left: 354px;
    width: 531px;
    height: 325px;
    background: var(--card);
    overflow: hidden;
  }
  .card--front { top: 79px; }
  .card--back { top: 463px; }

  .skyline-band {
    position: absolute;
    left: 0;
    right: 0;
    bottom: 0;
    height: 52px;
    background: var(--teal);
  }

  .contact {
    position: absolute;
    left: 243px;
    top: 152px;
    margin: 0;
    padding: 0;
    list-style: none;
  }
  .contact__item {
    display: flex;
    align-items: center;
    gap: 9px;
    height: 20px;
    margin-bottom: 14px;
    font-family: "Michroma", sans-serif;
    font-size: 9.5px;
    color: var(--ink);
    letter-spacing: 0.3px;
  }
  .contact__icon {
    width: 19px;
    height: 19px;
    flex: none;
  }

  .brand {
    position: absolute;
    right: 80px;
    top: 156px;
    text-align: right;
  }
  .brand__slogan {
    margin: 0 0 12px;
    font-family: "Jura", sans-serif;
    font-weight: 500;
    font-size: 15px;
    letter-spacing: 1.4px;
    color: var(--teal);
  }
  .brand__name {
    margin: 0;
    font-family: "Jura", sans-serif;
    font-weight: 600;
    font-size: 32px;
    line-height: 1;
    color: var(--ink);
    white-space: nowrap;
  }
</style>
</head>
<body>
<div class="canvas">

  <section class="card card--front" aria-label="Card front">
    <ul class="contact">
      <li class="contact__item">
        <svg class="contact__icon" viewBox="0 0 20 20" aria-hidden="true">
          <circle cx="10" cy="10" r="9" fill="var(--ink)"/>
          <g fill="none" stroke="var(--card)" stroke-width="1">
            <ellipse cx="10" cy="10" rx="4" ry="9"/>
            <line x1="1" y1="10" x2="19" y2="10"/>
            <line x1="2.5" y1="5.5" x2="17.5" y2="5.5"/>
            <line x1="2.5" y1="14.5" x2="17.5" y2="14.5"/>
            <line x1="10" y1="1" x2="10" y2="19"/>
          </g>
        </svg>
        <span>www.marlowecreative.works</span>
      </li>
      <li class="contact__item">
        <svg class="contact__icon" viewBox="0 0 20 20" aria-hidden="true">
          <circle cx="10" cy="10" r="8.6" fill="none" stroke="var(--ink)" stroke-width="1.4"/>
          <path d="M6.3 5.2l2 2.1-1 1.3c.7 1.6 2 2.9 3.6 3.6l1.3-1 2.1 2-1.2 1.6c-3.8-.5-7.3-4-7.9-7.9z" fill="var(--ink)"/>
        </svg>
        <span>000 000 00 00</span>
      </li>
    </ul>
    <div class="skyline-band" role="img" aria-label="City skyline silhouette in teal along the bottom edge"></div>
  </section>

  <section class="card card--back" aria-label="Card back">
    <div class="brand">
      <p class="brand__slogan">Simple Online Solutions</p>
      <p class="brand__name">Marlowe Creative Works</p>
    </div>
    <div class="skyline-band" role="img" aria-label="City skyline silhouette in teal along the bottom edge"></div>
  </section>

</div>
</body>
</html>
```